Honey packaging lable for small honey producer

We are small scale bee keepers and need a design for labels for our honey.
We curently sell honey in 2 different package sizes, 500gm and 1kg so the label would need to be suitable for both.
The plan is to print the label on brown or "craft" paper with a laser printer to give a rustic feel so the design will need to be monotone.
As we are in Australia all measurements will need to be metric
Label dimensions should be 105mm wide by 59.4mm high (so we can fit 10 labels per sheet of a4 paper).
The batch number, nett weight and number of servings per package on the nutritional label need to be able to be changed to suit the packaging size.
Designs need to be able to be opened and printed from open source software such as Free Desk, Pixo or similar. If proprietary software is used there must be at least a free program to allow printing and basic manipulation of the design.
Updates

Thank you everyone for the designs you submitted. I have been surprised by the quality of work supplied and wish I had the budget to make a payment to everyone, but unfortunately that is not the case :( 

This is my first time doing anything like this and it has been an interesting experience. I have definitely learned lots and hopefully I will be a better and more concise brief writer next time :)

The only other feedback I would like to give is to read the brief carefully. There were some designers that submited color designs which weren't suitable for my needs which may have been avoided.

Thank you again for all your hard work.

All the best.

Derek & Margot.

Industry/Entity Type

Printer

Requirements
Must have
• Brindlecote Farm
honey
Nett Weight
Batch Number:
Produced by: Derek and Margot Tollingham, Marbury Flat, Victoria. 0429 163072

Nutritional panel similar to : http://www.quillorbe.net.au/images/products/jars-pails-L030.jpg
Nice to have
• Produced in the Brannocks
Pure, Natural, raw.
Contains traces of pollen and wax
Honey is a natural product and may crystallize. It may be eaten as is or re-liquefied by placing the container in hot water.
Should not have
• No twee cartoon bees or skep bee hives please!

```html
<!DOCTYPE html>
<html lang="en">
<head>
<meta charset="utf-8">
<title>Brindlecote Farm Honey Label</title>
<link href="https://fonts.googleapis.com/css2?family=Orbitron:wght@700;900&family=Courier+Prime:wght@700&family=Cabin+Sketch&family=PT+Sans+Narrow:wght@400;700&display=swap" rel="stylesheet">
<style>
  :root {
    --page: #efe8d8;
    --kraft: #a8855b;
    --kraft-dark: #937148;
    --ink: #111010;
    --paper-text: #f4eee2;
  }
  * { box-sizing: border-box; margin: 0; padding: 0; }
  html, body { width: 1200px; height: 900px; overflow: hidden; background: var(--page); }
  .label {
    position: absolute; left: 50px; top: 140px;
    width: 1100px; height: 621px;
    background: var(--kraft);
    color: var(--ink);
    font-family: "PT Sans Narrow", "Arial Narrow", sans-serif;
    box-shadow: 0 10px 30px rgba(0,0,0,.25);
  }
  .rule { position: absolute; left: 0; right: 0; background: var(--ink); }
  .rule--top-thick { top: 14px; height: 10px; }
  .rule--top-thin { top: 32px; height: 4px; }
  .rule--bottom-thin { top: 569px; height: 4px; }
  .rule--bottom-thick { top: 581px; height: 10px; }

  .farm-name {
    position: absolute; left: 22px; top: 156px; width: 683px;
    font-family: "Orbitron", sans-serif; font-weight: 700;
    font-size: 45px; letter-spacing: 2px; text-transform: uppercase;
    white-space: nowrap; text-align: center;
  }
  .farm-underline { position: absolute; left: 22px; width: 683px; height: 3px; background: var(--ink); }
  .farm-underline--one { top: 211px; }
  .farm-underline--two { top: 219px; }

  .bee { position: absolute; background: var(--kraft-dark); border-radius: 6px; }
  .bee--left { left: 35px; top: 240px; width: 99px; height: 69px; }
  .bee--right { left: 587px; top: 240px; width: 89px; height: 69px; }
  .bee--lower { left: 420px; top: 424px; width: 98px; height: 73px; }

  .product {
    position: absolute; left: 150px; top: 222px; width: 421px;
    font-family: "Orbitron", sans-serif; font-weight: 900;
    font-size: 100px; line-height: 110px; letter-spacing: 2px;
    text-transform: uppercase; text-align: center;
  }
  .origin {
    position: absolute; left: 154px; top: 332px; width: 420px;
    font-family: "Courier Prime", "Courier New", monospace; font-weight: 700;
    font-size: 27px; white-space: nowrap;
  }
  .qualities {
    position: absolute; left: 154px; top: 366px;
    font-family: "Cabin Sketch", cursive; font-size: 40px; white-space: nowrap;
  }
  .net-weight {
    position: absolute; left: 22px; top: 470px;
    font-weight: 700; font-size: 28px; white-space: nowrap;
  }
  .net-weight span { margin-left: 18px; }
  .batch {
    position: absolute; left: 22px; top: 510px;
    font-weight: 700; font-size: 20px; white-space: nowrap;
  }
  .batch span { font-weight: 400; margin-left: 8px; letter-spacing: 1px; }
  .producer {
    position: absolute; right: 391px; top: 464px;
    text-align: right; font-weight: 700; font-size: 17px; line-height: 19.5px;
  }

  .nutrition-head {
    position: absolute; left: 731px; top: 59px; width: 366px; height: 99px;
    background: var(--ink); color: var(--paper-text);
    text-align: center; padding-top: 8px;
  }
  .nutrition-head h2 { font-size: 23px; font-weight: 700; line-height: 26px; }
  .nutrition-head p { font-size: 21px; line-height: 24px; }
  .nutrition-table {
    position: absolute; left: 764px; top: 166px; width: 330px;
    border-collapse: collapse; font-size: 17px; line-height: 21.5px;
  }
  .nutrition-table th { font-weight: 400; text-align: right; line-height: 19px; padding-bottom: 6px; }
  .nutrition-table td { font-weight: 700; text-align: right; padding: 0; }
  .nutrition-table td:first-child { text-align: left; }
  .nutrition-table .col-name { width: 120px; }
  .nutrition-table .col-serving { width: 92px; }
  .nutrition-notes {
    position: absolute; left: 731px; top: 382px; width: 366px;
    text-align: center; font-size: 16.5px; line-height: 21px;
  }
  .storage-note {
    position: absolute; left: 731px; top: 463px; width: 366px; height: 89px;
    background: var(--ink); color: var(--paper-text);
    text-align: center; font-size: 17px; line-height: 21.5px; padding: 12px 18px 0;
  }
</style>
</head>
<body>
<main class="label">
  <div class="rule rule--top-thick"></div>
  <div class="rule rule--top-thin"></div>

  <h1 class="farm-name">Brindlecote Farm</h1>
  <div class="farm-underline farm-underline--one"></div>
  <div class="farm-underline farm-underline--two"></div>

  <div class="bee bee--left" role="img" aria-label="Engraved-style honey bee illustration"></div>
  <div class="product">Honey</div>
  <div class="bee bee--right" role="img" aria-label="Engraved-style honey bee illustration"></div>

  <p class="origin">Produced in the Brannocks</p>
  <p class="qualities">Natural. Pure. Raw.</p>
  <div class="bee bee--lower" role="img" aria-label="Engraved-style honey bee illustration"></div>

  <p class="net-weight">Net Weight:<span>500g</span></p>
  <p class="batch">Batch Number:<span>130416</span></p>

  <address class="producer" style="font-style:normal">
    Produced by:<br>
    Derek &amp; Margot Tollingham<br>
    Marbury Flat<br>
    VICTORIA 0429 163072
  </address>

  <section class="nutrition-head">
    <h2>Nutritional information 500g</h2>
    <p>Servings per package: 33</p>
    <p>Serving Size: 15g</p>
  </section>

  <table class="nutrition-table">
    <tr>
      <th class="col-name"></th>
      <th class="col-serving">Quantity<br>Per Serving</th>
      <th>Quantity<br>Per 100g</th>
    </tr>
    <tr><td>Energy</td><td>214KJ</td><td>1416KJ</td></tr>
    <tr><td>Protein</td><td>.05g</td><td>.05g</td></tr>
    <tr><td>Fat - Total</td><td>0g</td><td>0g</td></tr>
    <tr><td>&nbsp;&nbsp;-Saturated</td><td>0g</td><td>0g</td></tr>
    <tr><td>Carbohydrates</td><td>12.5g</td><td>83.1g</td></tr>
    <tr><td>&nbsp;&nbsp;-sugars*</td><td>12.5g</td><td>82.5g</td></tr>
    <tr><td>Sodium</td><td>2.3mg</td><td>15mg</td></tr>
  </table>

  <p class="nutrition-notes">
    *Sugars naturally occuring in honey.<br>
    Ingredients: Pure 100% Australian Honey<br>
    Contains traces of pollen and wax.
  </p>

  <p class="storage-note">
    Honey is a natural product and may crystallize. It may be eaten as is or re-liquefied by placing the container in hot water.
  </p>

  <div class="rule rule--bottom-thin"></div>
  <div class="rule rule--bottom-thick"></div>
</main>
</body>
</html>
```